Lumen Path - Fiber Internet to the home postcard

Design a postcard for my company, Lumen Path, using the logo below. On the front of the card:
- No Buffering • No BS
- Second line should be the logo
- $60 / month • 10-Gigs
- lumenpath.net

Color palate should follow the colors in the logo.

Address should say
- Special pricing during construction
- Our best price
- Our fastest speed
- $60 / month • 10-Gigs
- lumenpath.net

Target Market(s)

25 - 55 year olds. Middle income/class. People with kids and pick up trucks

Industry/Entity Type

Fiber Internet Service Provider

Font styles to use
Sans Serif

Colors

Designer to choose colors to be used in the design.

Requirements
Nice to have
• I am open to more creative changes

```html
<!DOCTYPE html>
<html lang="en">
<head>
<meta charset="utf-8">
<title>Lumen Path – Fiber Postcard</title>
<link rel="stylesheet" href="https://fonts.googleapis.com/css2?family=Bebas+Neue&family=Roboto:wght@700;900&family=Roboto+Condensed:wght@700&family=Playfair+Display:ital,wght@1,600&display=swap">
<style>
  :root{
    --navy:#1b2a5c;
    --navy-deep:#14204a;
    --green:#7abf40;
    --green-mid:#5fa638;
    --green-dark:#2f5a22;
    --white:#ffffff;
    --paper:#f7f7f4;
    --line:#2a2a2a;
  }
  *{margin:0;padding:0;box-sizing:border-box}
  html,body{width:1029px;height:1200px;overflow:hidden;background:var(--paper)}
  .canvas{position:relative;width:1029px;height:1200px}
  .card{position:absolute;width:884px;height:590px;transform-origin:0 0;transform:scale(.95);overflow:hidden;box-shadow:0 2px 8px rgba(0,0,0,.18)}
  .card--front{left:94px;top:30px;background:linear-gradient(90deg,#dfe2e8 0%,#fff 12%,#fff 100%)}
  .card--back{left:94px;top:620px;background:var(--white)}

  /* front */
  .brand{position:absolute;left:76px;top:44px}
  .brand__name{font-family:"Roboto",sans-serif;font-weight:900;font-size:58px;line-height:1;color:var(--navy);letter-spacing:-1px}
  .photo-band{position:absolute;left:0;top:130px;width:884px;height:330px;background:linear-gradient(120deg,#4a5a7e 0%,#3b4d76 40%,#2c3d68 100%)}
  .offer-panel{position:absolute;left:497px;top:38px;width:330px;height:514px;background:var(--green)}
  .offer-panel__shade{position:absolute;left:0;top:92px;width:330px;height:330px;background:linear-gradient(160deg,#2c5a23 0%,#1f4520 60%,#2b5624 100%)}
  .band-edge{position:absolute;left:827px;top:130px;width:57px;height:330px;background:var(--navy-deep)}
  .price{position:absolute;left:557px;top:148px;font-family:"Bebas Neue",sans-serif;font-size:182px;line-height:1;color:var(--white)}
  .per-month{position:absolute;left:592px;top:300px;font-family:"Bebas Neue",sans-serif;font-size:44px;line-height:1;color:var(--white)}
  .speed{position:absolute;left:525px;top:384px;font-family:"Roboto",sans-serif;font-weight:700;font-size:62px;line-height:1;color:var(--white);letter-spacing:1px}
  .front-url{position:absolute;left:497px;width:330px;top:474px;text-align:center;font-family:"Roboto Condensed",sans-serif;font-weight:700;font-size:50px;line-height:1;color:var(--navy)}
  .tagline{position:absolute;left:42px;top:478px;font-family:"Roboto Condensed",sans-serif;font-weight:700;font-size:44px;line-height:1;color:var(--navy)}

  /* back */
  .back-panel{position:absolute;left:0;top:0;width:492px;height:590px;background:radial-gradient(circle at 70% 30%,#78b844 0%,var(--green-mid) 55%,#58a034 100%)}
  .divider{position:absolute;left:497px;top:0;width:6px;height:590px;background:var(--navy)}
  .pre-head{position:absolute;left:39px;top:30px;font-family:"Bebas Neue",sans-serif;font-size:40px;line-height:52px;color:#eef3e4}
  .lead{position:absolute;left:39px;font-family:"Bebas Neue",sans-serif;font-size:54px;line-height:1;color:var(--navy)}
  .lead--best{top:148px}
  .lead--fast{top:290px}
  .banner{position:absolute;left:39px;font-family:"Roboto Condensed",sans-serif;font-weight:700;font-size:66px;line-height:62px;height:62px;padding:0 2px;letter-spacing:-1px;white-space:nowrap}
  .banner--price{top:188px;width:322px;background:var(--white);color:var(--navy)}
  .banner--speed{top:330px;width:453px;background:var(--navy);color:var(--white)}
  .homes{position:absolute;left:360px;top:240px;width:118px;height:76px;border-radius:6px;background:linear-gradient(135deg,#3f7a2e,#1f4a1a)}
  .back-offer{position:absolute;left:39px;top:432px;font-family:"Bebas Neue",sans-serif;font-size:46px;line-height:1;color:var(--navy)}
  .back-url{position:absolute;left:39px;top:478px;font-family:"Roboto Condensed",sans-serif;font-weight:700;font-size:64px;line-height:1;color:var(--navy)}
  .stamp-box{position:absolute;left:742px;top:110px;width:94px;height:112px;border:1.5px solid var(--line);display:flex;align-items:center;justify-content:center;font-family:"Playfair Display",serif;font-style:italic;font-weight:600;font-size:17px;color:var(--line)}
  .address-line{position:absolute;left:517px;width:318px;height:1.5px;background:var(--line)}
</style>
</head>
<body>
<div class="canvas">

  <section class="card card--front" aria-label="Postcard front">
    <div class="brand">
      <span class="brand__name">Lumen Path</span>
    </div>
    <div class="photo-band" role="img" aria-label="Photo of a family relaxing together on a sofa with laptops and phones, navy tint"></div>
    <div class="offer-panel">
      <div class="offer-panel__shade" role="img" aria-label="Photo of a living room corner with plants, green tint"></div>
    </div>
    <div class="band-edge"></div>
    <div class="price">$60</div>
    <div class="per-month">/ Month</div>
    <div class="speed">10-GIGS</div>
    <div class="front-url">lumenpath.net</div>
    <div class="tagline">No Buffering • No BS</div>
  </section>

  <section class="card card--back" aria-label="Postcard address side">
    <div class="back-panel" role="img" aria-label="Green background with soft fiber-optic light strands"></div>
    <div class="pre-head">Special pricing during<br>construction</div>
    <div class="lead lead--best">Our</div>
    <div class="banner banner--price">BEST PRICE</div>
    <div class="homes" role="img" aria-label="Illustration of small houses connected by fiber cable"></div>
    <div class="lead lead--fast">Our</div>
    <div class="banner banner--speed">FASTEST SPEED</div>
    <div class="back-offer">$60 / Month 10-Gigs</div>
    <div class="back-url">lumenpath.net</div>
    <div class="divider"></div>
    <div class="stamp-box">Stamp</div>
    <div class="address-line" style="top:290px"></div>
    <div class="address-line" style="top:345px"></div>
    <div class="address-line" style="top:401px"></div>
    <div class="address-line" style="top:457px"></div>
  </section>

</div>
</body>
</html>
```